Website for a company focused on genealogical products and historical items

I need a website designed using our current branding.

Company name: R. L. Atelier: Merchants of Fine Heritage Prints

Our company sells ancestral art, downloadable worksheets pertaining to genealogy, and we offer weekend workshops and seminars.

the website should have the following pages:
landing page
products page: to include three different products: 1. a physical product with an intake form the customer completes online, 2. a downloadable product, and 3. a lecture/presentation booking page
about us page/history
contact page/sign up page

The website will include portraits of historical figures in gold frames, lots of white background, very clean design. We would like the website to feel fresh and clean, bright.

Target Market(s)

Older Americans interested in their family heritage and lineage

Industry/Entity Type

Genealogy, research, history, lectures

Coding

Coded - Design and coding required

Number of Pages Required

5+ page

Font styles to use
Serif
Other font styles liked:
• Libre Baskerville, Aliey, one historical script - P22 Royalist

Colors
0094D4
00A9DD
6FCCEA
C7EBF8
E9F6FB

Requirements
Must have
• must have our color branding and logo (pdf attached, and I can send original files), simple design, not too many images on each page (maybe one image per page)
Nice to have
• Nice to have clean design, all pages the same "look"
Should not have
• no black backgrounds, nothing too busy

```html
<!DOCTYPE html>
<html lang="en">
<head>
<meta charset="utf-8">
<title>R. L. Atelier: Merchants of Fine Heritage Prints</title>
<link href="https://fonts.googleapis.com/css2?family=Great+Vibes&family=Libre+Baskerville:wght@400;700&display=swap" rel="stylesheet">
<style>
:root{
  --blue:#0094D4;
  --blue-bright:#00A9DD;
  --blue-dark:#0079B0;
  --sky:#6FCCEA;
  --mist:#C7EBF8;
  --ice:#E9F6FB;
  --page:#F6FBFD;
  --text:#1B2B36;
  --muted:#00A9DD;
  --white:#FFFFFF;
  --gold-a:#5C4517;
  --gold-b:#E9D191;
  --gold-c:#8A6A24;
}
*{box-sizing:border-box;margin:0;padding:0}
html,body{width:1200px;height:3824px;overflow:hidden}
body{font-family:"Libre Baskerville",serif;color:var(--text);background:var(--page)}
.page{position:relative;width:1200px;height:3824px;overflow:hidden;background:var(--page)}
.abs{position:absolute}
a{color:inherit;text-decoration:none}

/* nav */
.site-nav{position:absolute;left:0;top:0;width:1200px;height:70px;background:var(--white);z-index:5;box-shadow:0 1px 0 var(--ice)}
.brand{position:absolute;left:150px;top:26px;font-size:13px;font-weight:700;color:var(--blue-dark);display:flex;align-items:center;gap:7px;white-space:nowrap}
.brand-mark{width:16px;height:16px;border:2px solid var(--blue);border-radius:50%}
.nav-links{position:absolute;left:288px;top:26px;display:flex;gap:24px;font-size:14.5px;color:var(--muted);white-space:nowrap}
.nav-links .active{color:var(--blue-dark);font-weight:700;position:relative}
.nav-links .active::after{content:"";position:absolute;left:-10px;right:-10px;top:40px;height:3px;background:var(--blue)}
.btn{display:inline-flex;align-items:center;justify-content:center;border-radius:5px;font-family:"Libre Baskerville",serif;font-weight:700;white-space:nowrap}
.btn-solid{background:var(--blue);color:var(--white)}
.btn-outline{background:var(--white);border:2px solid var(--blue);color:var(--text)}
.nav-contact{position:absolute;left:800px;top:15px;width:126px;height:39px;font-size:14.5px}
.nav-sign{position:absolute;left:934px;top:15px;width:116px;height:39px;font-size:14.5px;border-color:var(--sky)}

/* hero */
.guide-line{position:absolute;left:0;top:70px}
.hero-title{left:150px;top:204px;font-family:"Great Vibes",cursive;font-size:62px;line-height:70px;color:var(--text);font-weight:400;white-space:nowrap}
.hero-copy{left:150px;top:364px;width:400px;font-size:15.5px;line-height:26px}
.hero-btn{left:150px;top:497px;width:217px;height:43px;font-size:15px;box-shadow:0 3px 5px rgba(0,80,120,.2)}
.hero-arch{left:650px;top:118px;width:478px;height:557px;border-radius:239px 239px 0 0 / 160px 160px 0 0;background:radial-gradient(ellipse at 50% 45%,#A77A4E 0%,#6B4B2D 45%,#2E2418 100%)}
.hero-base{left:650px;top:675px;width:550px;height:15px;background:var(--mist)}

/* about */
.about-block{left:150px;top:842px;width:330px;height:316px;border-radius:16px;background:var(--blue)}
.gold-frame{padding:10px;background:linear-gradient(135deg,var(--gold-a),var(--gold-b) 40%,var(--gold-c) 70%,var(--gold-b));box-shadow:0 6px 12px rgba(0,0,0,.25)}
.photo{width:100%;height:100%}
.photo-carving{background:radial-gradient(ellipse at 50% 40%,#A57A4F,#5A3F25 60%,#2D2218)}
.about-photo{left:200px;top:885px;width:328px;height:318px;transform:rotate(-5deg);border-radius:10px}
.eyebrow{font-size:15px;color:var(--text);display:flex;align-items:center;gap:10px;letter-spacing:.3px;white-space:nowrap}
.eyebrow::before{content:"";width:36px;height:1px;background:var(--text)}
.section-title{font-size:33px;line-height:40px;font-weight:400;white-space:nowrap}
.body-small{font-size:10.8px;line-height:22.5px}
.about-eyebrow{left:615px;top:840px}
.about-title{left:615px;top:864px}
.about-copy{left:615px;top:955px;width:440px}
.about-btn{left:615px;top:1130px;width:219px;height:42px;font-size:15px;border-color:var(--sky)}

/* explore */
.explore-eyebrow{left:150px;top:1413px}
.explore-title{left:150px;top:1438px}
.explore-copy{left:150px;top:1529px;width:440px}
.explore-btn{left:150px;top:1704px;width:219px;height:42px;font-size:15px;border-color:var(--sky)}
.explore-big{left:767px;top:1396px;width:283px;height:354px}
.explore-small{left:650px;top:1540px;width:200px;height:210px;transform:rotate(-12deg)}
.photo-temple{background:linear-gradient(160deg,#7E5C3C,#4A3422 55%,#2F2217)}
.photo-statue{background:linear-gradient(160deg,#A88356,#CDB89C 50%,#8C7558)}

/* family band */
.family-band{left:0;top:1960px;width:1200px;height:412px;background:var(--mist)}
.family-art{left:315px;top:2025px;width:570px;height:325px;border-radius:12px;background:linear-gradient(180deg,#D9F1FA,#B5E3F4)}

/* worksheets */
.sheet-band{left:0;top:2372px;width:1200px;height:136px;background:var(--blue);color:var(--white)}
.sheet-title{position:absolute;left:150px;top:46px;font-size:25px;font-weight:400;white-space:nowrap}
.sheet-sub{position:absolute;left:150px;top:83px;font-size:10.5px;opacity:.95;white-space:nowrap}
.sheet-btn{position:absolute;left:822px;top:48px;width:228px;height:42px;font-size:15px;background:var(--white);color:var(--text);border-radius:5px;box-shadow:0 3px 5px rgba(0,60,100,.25)}

/* workshops */
.events-head{left:0;top:2672px;width:1200px;text-align:center}
.events-eyebrow{font-size:15px;letter-spacing:.3px}
.events-title{font-size:33px;line-height:39px;font-weight:400;margin-top:12px}
.events-rule{width:62px;height:4px;background:var(--blue-dark);margin:8px auto 0}
.event-card{position:absolute;top:2830px;width:288px;height:355px;background:var(--white);border-radius:6px;box-shadow:0 4px 14px rgba(0,90,140,.12);padding:16px 17px}
.event-img{width:254px;height:156px;border-radius:3px}
.img-relief{background:linear-gradient(160deg,#CFC3AE,#A8987E)}
.img-ceremony{background:linear-gradient(160deg,#4A3C33,#B46B4A 50%,#6A3F44)}
.img-gallery{background:linear-gradient(160deg,#6F675C,#A79C8B 55%,#5C564E)}
.event-title{font-size:21px;font-weight:400;margin-top:22px;white-space:nowrap}
.event-copy{font-size:10.5px;line-height:18px;margin-top:10px}
.event-meta{font-size:10.5px;line-height:18px;margin-top:16px}
.event-meta span{color:var(--muted)}
.event-go{position:absolute;right:17px;bottom:18px;width:44px;height:42px;background:var(--blue);border-radius:5px;display:flex;align-items:center;justify-content:center}
.view-more{left:534px;top:3210px;width:130px;height:38px;font-size:12.5px;border-color:var(--sky);box-shadow:0 2px 4px rgba(0,60,100,.15)}

/* footer */
.footer-bg{left:0;top:3520px;width:1200px;height:265px;background:var(--blue)}
.news-card{left:150px;top:3415px;width:900px;height:170px;background:var(--white);border-radius:14px;box-shadow:0 4px 14px rgba(0,60,100,.1);text-align:center}
.news-title{font-size:31px;font-weight:400;margin-top:38px}
.news-copy{font-size:10.5px;margin-top:16px}
.news-form{display:flex;width:327px;height:33px;margin:20px auto 0;border:1.5px solid var(--mist);border-radius:3px;overflow:hidden;box-shadow:0 2px 4px rgba(0,60,100,.12)}
.news-input{flex:1;background:var(--ice);font-size:10.5px;text-align:left;padding:10px 14px}
.news-btn{width:98px;background:var(--blue);color:var(--white);font-size:11px;display:flex;align-items:center;justify-content:center}
.footer-brand{left:262px;top:3636px;width:113px;height:94px;background:var(--white);border-radius:3px;display:flex;align-items:center;justify-content:center;text-align:center;font-size:10.5px;font-weight:700;color:var(--blue-dark);padding:8px;line-height:15px}
.footer-col{position:absolute;top:3640px;color:var(--white)}
.footer-col h4{font-size:13px;font-weight:400;margin-bottom:6px}
.footer-col p{font-size:8.5px;line-height:13px}
.copyright{left:0;top:3785px;width:1200px;height:39px;background:var(--ice);font-size:8px;color:var(--blue-dark);text-align:center;line-height:39px}
</style>
</head>
<body>
<div class="page">

  <svg class="guide-line" width="1200" height="1700" viewBox="0 70 1200 1700" aria-hidden="true">
    <path d="M520 70 V700 C520 1100 300 1520 0 1760" fill="none" stroke="#C7EBF8" stroke-width="14"/>
  </svg>

  <header class="site-nav">
    <a class="brand" href="#"><span class="brand-mark"></span>R. L. Atelier</a>
    <nav class="nav-links">
      <a class="active" href="#">Home</a>
      <a href="#">About Us</a>
      <a href="#">Our Products</a>
      <a href="#">Workshops</a>
      <a href="#">Seminars</a>
    </nav>
    <a class="btn btn-solid nav-contact" href="#">Contant Us</a>
    <a class="btn btn-outline nav-sign" href="#">Sign In</a>
  </header>

  <section class="hero">
    <h1 class="abs hero-title">A Center for Family<br>Heritage and Lineage</h1>
    <p class="abs hero-copy">Lorem ipsum dolor sit amet consectetur. Leo in et mauris donec. Ut orci massa venenatis pulvinar viverra enim tempus enim commodo. Nulla at ultricies nulla</p>
    <a class="abs btn btn-solid hero-btn" href="#">Get Started Today</a>
    <div class="abs hero-arch" role="img" aria-label="Carved temple relief of a standing deity in warm bronze light"></div>
    <div class="abs hero-base"></div>
  </section>

  <section class="about">
    <div class="abs about-block"></div>
    <div class="abs gold-frame about-photo"><div class="photo photo-carving" role="img" aria-label="Carved relief of a standing figure in a gold frame"></div></div>
    <div class="abs eyebrow about-eyebrow">ABOUT US</div>
    <h2 class="abs section-title about-title">Celebrating Ancestral<br>Connections through Art</h2>
    <p class="abs body-small about-copy">Lorem ipsum dolor sit amet consectetur. Leo in et mauris donec. Ut orci massa venenatis pulvinar viverra enim tempus enim commodo. Nulla at ultricies nullaLorem ipsum dolor sit amet consectetur. Leo in et mauris donec. Ut orci massa venenatis pulvinar viverra enim tempus enim commodo. Nulla at ultricies nullaLorem ipsum dolor sit amet consectetur. Leo in et mauris donec. Ut orci massa venenatis pulvinar viverra enim tempus enim commodo. Nulla at ultricies nullaLorem ipsum dolor sit</p>
    <a class="abs btn btn-outline about-btn" href="#">Join Our Community</a>
  </section>

  <section class="explore">
    <div class="abs eyebrow explore-eyebrow">EXPLORE THE ANCESTRAL ART</div>
    <h2 class="abs section-title explore-title">Immerse Yourself<br>in Ancestral Art</h2>
    <p class="abs body-small explore-copy">Lorem ipsum dolor sit amet consectetur. Leo in et mauris donec. Ut orci massa venenatis pulvinar viverra enim tempus enim commodo. Nulla at ultricies nullaLorem ipsum dolor sit amet consectetur. Leo in et mauris donec. Ut orci massa venenatis pulvinar viverra enim tempus enim commodo. Nulla at ultricies nullaLorem ipsum dolor sit amet consectetur. Leo in et mauris donec. Ut orci massa venenatis pulvinar viverra enim tempus enim commodo. Nulla at ultricies nullaLorem ipsum</p>
    <a class="abs btn btn-outline explore-btn" href="#">Discover More</a>
    <div class="abs gold-frame explore-big"><div class="photo photo-temple" role="img" aria-label="Intricately carved wooden temple interior"></div></div>
    <div class="abs gold-frame explore-small"><div class="photo photo-statue" role="img" aria-label="Stone guardian lion statue before a temple"></div></div>
  </section>

  <section class="abs family-band"></section>
  <div class="abs family-art" role="img" aria-label="Illustrated family tree of grandparents, parents and children joined by connecting lines"></div>

  <section class="abs sheet-band">
    <h3 class="sheet-title">Downloadable Worksheets Pertaining To Genealogy</h3>
    <p class="sheet-sub">Lorem Ipsum Dolor Sit Amet Consectetur. Leo In Et Mauris Donec. Ut Orci Massa Venenatis Pulvinar Viverra E</p>
    <a class="btn sheet-btn" href="#">Download Worksheets</a>
  </section>

  <section class="events">
    <div class="abs events-head">
      <p class="events-eyebrow">UPCOMING WORKSHOPS &amp; SEMINARS</p>
      <h2 class="events-title">Engage in<br>Interactive Workshops &amp; Seminars</h2>
      <div class="events-rule"></div>
    </div>

    <article class="event-card" style="left:150px">
      <div class="event-img img-relief" role="img" aria-label="Stone relief of a seated meditating figure"></div>
      <h3 class="event-title">Lorem ipsum dolor</h3>
      <p class="event-copy">Lorem ipsum dolor sit amet consectetur. Leo in et mauris donec. Ut orci massa venenatis pulvin ar viverra e</p>
      <p class="event-meta"><span>Time:</span> 09:30 am - 1:30 pm<br><span>Venue:</span> Online Meeting Room<br><span>Date:</span> 12th May 2024 (Sunday)</p>
      <a class="event-go" href="#" aria-label="Open workshop"><svg width="20" height="20" viewBox="0 0 20 20"><path d="M3 10h13M10 4l6 6-6 6" fill="none" stroke="#fff" stroke-width="2.4" stroke-linecap="round" stroke-linejoin="round"/></svg></a>
    </article>
    <article class="event-card" style="left:455px">
      <div class="event-img img-ceremony" role="img" aria-label="Hands holding a ceremonial fire offering"></div>
      <h3 class="event-title">Lorem ipsum dolor</h3>
      <p class="event-copy">Lorem ipsum dolor sit amet consectetur. Leo in et mauris donec. Ut orci massa venenatis pulvin ar viverra e</p>
      <p class="event-meta"><span>Time:</span> 09:30 am - 1:30 pm<br><span>Venue:</span> Online Meeting Room<br><span>Date:</span> 12th May 2024 (Sunday)</p>
      <a class="event-go" href="#" aria-label="Open workshop"><svg width="20" height="20" viewBox="0 0 20 20"><path d="M3 10h13M10 4l6 6-6 6" fill="none" stroke="#fff" stroke-width="2.4" stroke-linecap="round" stroke-linejoin="round"/></svg></a>
    </article>
    <article class="event-card" style="left:761px">
      <div class="event-img img-gallery" role="img" aria-label="Museum display of antique figurines and framed icons"></div>
      <h3 class="event-title">Lorem ipsum dolor</h3>
      <p class="event-copy">Lorem ipsum dolor sit amet consectetur. Leo in et mauris donec. Ut orci massa venenatis pulvin ar viverra e</p>
      <p class="event-meta"><span>Time:</span> 09:30 am - 1:30 pm<br><span>Venue:</span> Online Meeting Room<br><span>Date:</span> 12th May 2024 (Sunday)</p>
      <a class="event-go" href="#" aria-label="Open seminar"><svg width="20" height="20" viewBox="0 0 20 20"><path d="M3 10h13M10 4l6 6-6 6" fill="none" stroke="#fff" stroke-width="2.4" stroke-linecap="round" stroke-linejoin="round"/></svg></a>
    </article>

    <a class="abs btn btn-outline view-more" href="#">View More</a>
  </section>

  <footer>
    <div class="abs footer-bg"></div>
    <div class="abs news-card">
      <h2 class="news-title">Newsletter Sign up for Update</h2>
      <p class="news-copy">Lorem ipsum dolor sit amet consectetur. Leo in et mauris donec. Ut orci massa venenatis pulvinar viverra e</p>
      <div class="news-form"><span class="news-input">Enter Your Email</span><span class="news-btn">Sign Up</span></div>
    </div>

    <div class="abs footer-brand">R. L. Atelier: Merchants of Fine Heritage Prints</div>

    <div class="footer-col" style="left:441px">
      <h4>Contact Info</h4>
      <p>48 Orchard Lane,<br>Hollowmere Quarter,<br>Hollowmere, ST 20418</p>
      <p style="margin-top:6px">555 014 2290</p>
      <p style="margin-top:6px">hello@rlatelier.example</p>
    </div>
    <div class="footer-col" style="left:603px">
      <h4>Links</h4>
      <p>Home<br>About Us<br>Our Products<br>Workshops<br>Seminars</p>
    </div>
    <div class="footer-col" style="left:720px">
      <h4>Legal</h4>
      <p>Cookie Policy<br>Privacy Policy<br>Terms of Services</p>
    </div>
    <div class="footer-col" style="left:862px">
      <h4>Connected</h4>
      <p>Community Page<br>Photo Journal<br>News Updates<br>Video Talks</p>
    </div>

    <p class="abs copyright">Copyright © 2024 All rights reserved</p>
  </footer>

</div>
</body>
</html>
```